Vyrella Motion Design
Would like the design to go over the page in a way that can type over it.
We are a personal training and small group studio
Want it to be professional and classy
Reason: Asked for some modifications on a few designs, want to give the designers time to do this
Target Market(s)
All age groups, sports professionals as well as business professionals, families
Industry/Entity Type
Training
Requirements
Must have
- Must have Vyrella Motion Studio
Mira Pendleby
314 Calloway Street
Marbeck Vale
Southern Region 7214
Phone: 0497318260
Nice to have
- Professional classy fonts
Colour
Should not have
- Clip art
Balloons

```html
<!DOCTYPE html>
<html lang="en">
<head>
<meta charset="utf-8">
<title>Vyrella Motion Studio – Letterhead</title>
<link rel="stylesheet" href="https://fonts.googleapis.com/css2?family=Arimo:wght@400;700&family=Great+Vibes&family=Questrial&display=swap">
<style>
  :root {
    --ink: #111111;
    --brand-blue: #1e63c8;
    --accent-orange: #f07f1e;
    --rule-blue: #1a3f9a;
    --band-deep: #0a3d9e;
    --band-cyan: #00c3f4;
    --contact-ink: #5a5a5a;
    --paper: #ffffff;
  }
  html, body {
    margin: 0;
    padding: 0;
    overflow: hidden;
    background: var(--paper);
  }
  .letterhead {
    position: relative;
    width: 922px;
    height: 1200px;
    background: var(--paper);
    overflow: hidden;
    font-family: "Arimo", Arial, sans-serif;
    color: var(--ink);
  }
  .brand-name {
    position: absolute;
    left: 62px;
    top: 66px;
    margin: 0;
    font-family: "Arimo", Arial, sans-serif;
    font-weight: 700;
    font-size: 24px;
    line-height: 1;
    color: var(--brand-blue);
    white-space: nowrap;
  }
  .header-rule {
    position: absolute;
    left: 615px;
    top: 36px;
    width: 2px;
    height: 80px;
    background: linear-gradient(to bottom, rgba(26,63,154,0), var(--rule-blue) 30%, var(--rule-blue) 70%, rgba(26,63,154,0));
  }
  .contact {
    position: absolute;
    left: 686px;
    top: 28px;
    margin: 0;
    padding: 0;
    list-style: none;
    font-family: "Questrial", "Century Gothic", sans-serif;
    font-size: 9px;
    line-height: 11px;
    color: var(--contact-ink);
  }
  .contact li {
    display: flex;
    align-items: flex-start;
    gap: 6px;
    margin-bottom: 4px;
  }
  .contact-icon {
    width: 11px;
    height: 11px;
    flex: none;
  }
  .salutation {
    position: absolute;
    left: 97px;
    top: 209px;
    margin: 0;
    font-size: 16px;
  }
  .letter-body {
    position: absolute;
    left: 162px;
    top: 240px;
    width: 660px;
  }
  .letter-body p {
    margin: 0 0 19px;
    font-size: 15.3px;
    line-height: 19.2px;
    width: 642px;
  }
  .signature {
    position: absolute;
    left: 88px;
    top: 846px;
    margin: 0;
    font-family: "Great Vibes", cursive;
    font-size: 44px;
    line-height: 1;
  }
  .signatory-role {
    position: absolute;
    left: 118px;
    top: 898px;
    margin: 0;
    font-size: 16px;
  }
  .footer-band {
    position: absolute;
    left: 0;
    top: 1000px;
    width: 922px;
    height: 200px;
    display: block;
  }
</style>
</head>
<body>
<main class="letterhead">
  <header>
    <p class="brand-name">Vyrella Motion Studio</p>
    <div class="header-rule"></div>
    <ul class="contact">
      <li>
        <svg class="contact-icon" viewBox="0 0 12 12"><circle cx="6" cy="6" r="6" fill="var(--accent-orange)"/><path d="M3 6.3 6 3.5 9 6.3V9H3Z" fill="#fff"/></svg>
        <span>Mira Pendleby<br>314 Calloway Street<br>Marbeck Vale<br>Southern Region 7214</span>
      </li>
      <li>
        <svg class="contact-icon" viewBox="0 0 12 12"><circle cx="6" cy="6" r="6" fill="var(--accent-orange)"/><path d="M4 3.2c.5 0 1 1.2 1 1.5s-.6.5-.4 1 1 1.3 1.4 1.4.6-.5 1-.4 1.4.6 1.4 1-.8 1.3-1.5 1.1S4.4 8.2 3.6 6.4 3.4 3.2 4 3.2Z" fill="#fff"/></svg>
        <span>0497318260</span>
      </li>
      <li>
        <svg class="contact-icon" viewBox="0 0 12 12"><circle cx="6" cy="6" r="6" fill="var(--accent-orange)"/><rect x="3.5" y="3" width="5" height="6" rx=".6" fill="#fff"/><rect x="4.4" y="4" width="3.2" height="1.4" fill="var(--accent-orange)"/></svg>
        <span>+000 000 0000</span>
      </li>
      <li>
        <svg class="contact-icon" viewBox="0 0 12 12"><circle cx="6" cy="6" r="6" fill="var(--accent-orange)"/><rect x="3" y="4" width="6" height="4.2" fill="#fff"/><path d="M3 4 6 6.4 9 4" fill="none" stroke="var(--accent-orange)" stroke-width=".7"/></svg>
        <span>hello@vyrellamail.com</span>
      </li>
      <li>
        <svg class="contact-icon" viewBox="0 0 12 12"><circle cx="6" cy="6" r="6" fill="var(--accent-orange)"/><circle cx="6" cy="6" r="3" fill="none" stroke="#fff" stroke-width=".8"/><path d="M3 6h6M6 3c-1.3 1.8-1.3 4.2 0 6M6 3c1.3 1.8 1.3 4.2 0 6" fill="none" stroke="#fff" stroke-width=".6"/></svg>
        <span>www.vyrellamotionstudio.com</span>
      </li>
    </ul>
  </header>

  <p class="salutation">Dear Sir / Madam,</p>

  <section class="letter-body">
    <p>Lorem ipsum dolor sit amet, consectetur adipisicing elit, sed do eiusmod tempor labore et olore magna aliqua. Ut enim ad minim veniam, quis nostrud exercitation ullamco laboris nisi ut aliquip ex ea commodo consequa.Lorem ipsum dolor sit amet, nsectetur adipisicing elit, sed do eiusmod tempor incididunt ut labore et dolore magna aliqua. Ut enim ad minim veniam, quis.</p>
    <p>Lorem ipsum dolor sit amet, consectetur adipisicing elit, sed do eiusmod tempor labore et dolore magna aliqua. Ut enim ad minim veniam, quis nostrud exercitation ullamco laboris nisi ut aliquip ex ea commodo consequa.Lorem ipsum dolor sit amet, nsectetur adipisicing elit, sed do eiusmod tempor incididunt ut labore et dolore magna aliqua. Ut enim ad minim veniam, quis.</p>
    <p>Lorem ipsum dolor sit amet, consectetur adipisicing elit, sed do eiusmod tempor labore et dolore magna aliqua. Ut enim ad minim veniam, quis nostrud exercitation ullamco laboris nisi ut aliquip ex ea commodo consequa.Lorem ipsum dolor sit amet, nsectetur adipisicing elit, sed do eiusmod tempor incididunt ut labore et dolore magna aliqua. Ut enim ad minim veniam, quis.</p>
    <p>Lorem ipsum dolor sit amet, consectetur adipisicing elit, sed do eiusmod tempor labore et dolore magna aliqua. Ut enim ad minim veniam, quis nostrud exercitation ullamco laboris nisi ut aliquip ex ea commodo consequa.Lorem ipsum dolor sit amet, nsectetur adipisicing elit, sed do eiusmod tempor incididunt ut labore et dolore magna aliqua. Ut enim ad minim veniam, quis.</p>
    <p>Lorem ipsum dolor sit amet, consectetur adipisicing elit, sed do eiusmod tempor labore et dolore magna aliqua. Ut enim ad minim veniam, quis nostrud exercitation ullamco laboris nisi ut aliquip ex ea commodo consequa.Lorem ipsum dolor sit amet, nsectetur adipisicing elit, sed do eiusmod tempor incididunt ut labore et dolore magna aliqua. Ut enim ad minim veniam, quis.</p>
  </section>

  <p class="signature">Your Name</p>
  <p class="signatory-role">Company Director</p>

  <svg class="footer-band" viewBox="0 0 922 200" preserveAspectRatio="none" aria-hidden="true">
    <path d="M0 150 L922 40 L922 200 L0 200 Z" fill="var(--band-deep)"/>
    <path d="M0 182 L922 140 L922 200 L0 200 Z" fill="var(--band-cyan)"/>
  </svg>
</main>
</body>
</html>
```